Networking Events Calendar/Diary

We need a responsive website that can act as both an online diary/calendar and a resource for community and networking events similar to lookupmixerdates.com (we do not want a clone, but one with similar functionality). We need to be able to host adverts, have a client area for clients to add their own events to the diary. This needs to have the functionality that clients have to pay to add recurring events. Some integration would be useful so that if a clients already has their own online diary on their website then using an API possibly to also add that event into our online diary

Industry/Entity Type

Events

Coding

Coded - Design and coding required

Number of Pages Required

5+ page

Requirements
Must have
• My project must have a calendar area, space for ads, be responsive and easily viewable on mobile. A subscribers area for clients and a way to purchase premium status so that premium events are highlighted.

```html
<!DOCTYPE html>
<html lang="en">
<head>
<meta charset="utf-8">
<title>MeetDiary – Networking Events Diary</title>
<link href="https://fonts.googleapis.com/css2?family=Open+Sans:wght@400;600;700&family=Raleway:wght@500;600;700&display=swap" rel="stylesheet">
<style>
:root{
  --navy:#0f3a63;
  --navy-dark:#0b2c4c;
  --navy-light:#1f5a8e;
  --orange:#f5a623;
  --orange-dark:#e08f0c;
  --heading:#1b3e66;
  --text:#666;
  --text-dark:#222;
  --rule:#e3e3e3;
  --bg:#ffffff;
  --footer-top:#1e5687;
  --footer-bottom:#123a60;
  --footer-bar:#0e2f50;
}
*{box-sizing:border-box;margin:0;padding:0}
html,body{width:1200px;height:3482px;overflow:hidden;background:var(--bg)}
body{position:relative;font-family:"Open Sans",Arial,sans-serif;color:var(--text)}
a{color:inherit;text-decoration:none}
.abs{position:absolute}

/* Header */
.brand{left:100px;top:22px}
.brand-name{font-family:"Open Sans",sans-serif;font-weight:600;font-size:38px;color:var(--navy);letter-spacing:-1px}
.brand-tag{font-size:12px;color:#444;margin-top:4px}
.search{left:582px;top:46px;width:38px;height:38px;border-radius:50%;background:#e4e4e4}
.top-link{top:56px;font-size:12px;color:#333}
.login{left:1008px;top:48px;width:92px;height:34px;background:var(--orange);color:#fff;font-size:12px;font-weight:700;text-align:center;line-height:34px;border-radius:2px}

/* Nav */
.nav{left:0;top:118px;width:1200px;height:56px;background:var(--navy)}
.nav ul{list-style:none;display:flex;position:absolute;left:100px;top:0;height:56px}
.nav li{font-family:"Raleway",sans-serif;font-weight:600;font-size:15px;color:#fff;line-height:56px;padding:0 23px;border-right:1px solid rgba(255,255,255,.18)}
.nav li.active{background:var(--navy-light)}
.nav li:last-child{border-right:0}

/* Hero */
.hero{left:0;top:174px;width:1200px;height:425px;background:linear-gradient(100deg,#5a5f66 0%,#9a9890 35%,#c9c2b8 55%,#7f7e7c 80%,#b9b3aa 100%)}
.hero-text{left:135px;top:170px;color:#fff}
.hero-text h1{font-family:"Raleway",sans-serif;font-weight:700;font-size:30px;letter-spacing:.5px}
.hero-text p{font-size:18px;line-height:30px;margin-top:10px;width:520px}
.dots{left:562px;top:385px;display:flex;gap:10px}
.dots span{width:10px;height:10px;border-radius:50%;background:rgba(255,255,255,.55)}
.dots span.on{background:#fff}

/* Section headings */
.sec-title{font-family:"Open Sans",sans-serif;font-weight:700;font-size:15px;color:var(--heading);text-transform:uppercase;width:712px;padding-bottom:16px;border-bottom:1px solid var(--rule)}
.side-title{font-weight:700;font-size:14px;color:var(--heading);text-transform:uppercase;width:257px;padding-bottom:12px;border-bottom:1px solid var(--rule)}
.arrows{left:748px;top:630px;display:flex;gap:4px}
.arrows span{width:30px;height:30px;border:1px solid #ccc;display:flex;align-items:center;justify-content:center}

/* Tips grid */
.tip{width:213px}
.tip .ph{width:213px;height:139px}
.tip h3{font-size:11px;font-weight:700;color:var(--text-dark);line-height:21px;margin-top:12px;text-transform:uppercase}
.tip p{font-size:11px;line-height:21px;margin-top:6px}

.banner{left:148px;top:1306px;width:625px;height:77px;background:linear-gradient(90deg,#f08a17 0%,#f6b24b 30%,#1a1a1a 30%,#2a2a2a 70%,#d9d6cf 70%,#c9c3b8 100%)}

/* Events list */
.event{left:100px;width:712px;height:220px;border-bottom:1px solid var(--rule)}
.event .ph{position:absolute;left:0;top:0;width:213px;height:155px}
.event .body{position:absolute;left:248px;top:0;width:464px}
.event h3{font-size:12px;font-weight:700;color:var(--text-dark);text-transform:uppercase;margin-top:2px}
.meta{display:flex;gap:28px;font-size:9px;color:#999;margin-top:18px;align-items:center}
.meta span{display:flex;align-items:center;gap:6px}
.event p{font-size:11.5px;line-height:26px;margin-top:16px;color:#666}

.pager{left:420px;top:2561px;display:flex;gap:6px}
.pager span{height:26px;min-width:26px;padding:0 8px;border:1px solid #ccc;font-size:11px;color:#333;line-height:24px;text-align:center}

/* News */
.news{width:340px}
.news h3{font-size:13px;font-weight:700;color:var(--text-dark);text-transform:uppercase;line-height:24px}
.news .bar{width:34px;height:3px;background:var(--orange);margin-top:8px}
.news p{font-size:12px;line-height:24px;margin-top:18px}

/* Sidebar */
.social{display:flex;gap:6px}
.social span{width:28px;height:28px;border-radius:50%}
.cal{left:845px;top:812px;width:257px;height:209px;border:1px solid var(--rule)}
.cal-head{height:32px;display:flex;justify-content:space-between;align-items:center;background:#eee}
.cal-head b{font-size:11px;color:var(--heading)}
.cal-head span{width:16px;height:32px;background:var(--navy-light);display:flex;align-items:center;justify-content:center}
.cal-card{position:absolute;left:10px;top:44px;width:235px;height:96px;background:var(--navy);color:#fff}
.cal-card .ph{position:absolute;left:12px;top:14px;width:60px;height:56px;background:linear-gradient(135deg,#c9d6e3,#7b93ad)}
.cal-card b{position:absolute;left:84px;top:14px;font-size:10px;line-height:16px;width:140px}
.cal-card i{position:absolute;left:84px;top:52px;font-style:normal;font-size:11px}
.cal-days{position:absolute;left:10px;top:160px;display:flex;gap:4px}
.cal-days span{width:26px;height:26px;background:#f3f3f3;font-size:9px;color:#999;text-align:center;line-height:26px}
.cal-days span.on{background:#8aa36b;color:#fff}

.promo{left:845px;width:257px;height:237px}
.promo .ph{position:absolute;inset:0}
.promo .cap{position:absolute;left:0;bottom:0;width:190px;height:72px;background:rgba(15,58,99,.92);color:#fff;padding:14px 18px}
.promo .cap b{font-size:12px;font-weight:700;display:block}
.promo .cap span{font-size:10px;display:block;margin-top:6px}

.vids{left:845px;top:1833px;display:grid;grid-template-columns:122px 122px;gap:12px 12px}
.vid{height:88px;position:relative}
.vid svg{position:absolute;left:46px;top:29px}
.more{left:845px;top:2148px;width:160px;height:40px;background:var(--orange);color:#fff;font-size:11px;font-weight:700;line-height:40px;text-align:center}

.tweets{left:845px;top:2211px;width:257px;height:457px;border:1px solid #ddd;background:#fff}
.tw-head{height:42px;border-bottom:1px solid #e6e6e6;display:flex;justify-content:space-between;align-items:center;padding:0 12px}
.tw-head b{font-size:14px;color:#222}
.tw-head span{font-size:10px;border:1px solid #ccc;border-radius:3px;padding:2px 8px;color:#333}
.tw{display:flex;gap:12px;padding:12px;height:92px;border-bottom:1px solid #eee}
.tw .av{width:62px;height:62px;background:var(--orange);flex:none}
.tw p{font-size:11px;line-height:18px;color:#333}
.tw p b{font-weight:700}
.tw-input{position:absolute;left:12px;bottom:10px;width:231px;height:26px;border:1px solid #ccc;font-size:10px;color:#999;padding:5px 8px}

.ad-side{left:845px;width:257px}

/* Footer */
.footer{left:0;top:3144px;width:1200px;height:266px;background:linear-gradient(180deg,var(--footer-top),var(--footer-bottom))}
.f-col{top:40px;color:#fff}
.f-col h4{font-family:"Raleway",sans-serif;font-weight:500;font-size:21px;margin-bottom:12px}
.f-col li{list-style:none;font-size:12px;line-height:26px;color:#dce6f0}
.f-col p{font-size:12px;color:#dce6f0}
.f-input{width:265px;height:36px;background:#fff;margin-top:14px;display:flex;align-items:center;gap:8px;padding:0 10px;font-size:11px;color:#888}
.f-btn{width:120px;height:38px;background:var(--orange);font-size:13px;font-weight:600;text-align:center;line-height:38px;margin-top:10px}
.f-social{display:flex;gap:8px;margin-top:4px}
.f-social span{width:36px;height:36px;border:2px solid #fff;border-radius:50%}
.bottom{left:0;top:3410px;width:1200px;height:72px;background:var(--footer-bar);color:#9fb3c8;font-size:11px}
.bottom p{position:absolute;left:108px;top:28px}
</style>
</head>
<body>

<header>
  <div class="abs brand">
    <div class="brand-name">MeetDiary</div>
    <div class="brand-tag">We are an online diary/calendar and a resource for networking events</div>
  </div>
  <div class="abs search">
    <svg width="38" height="38" viewBox="0 0 38 38"><circle cx="18" cy="18" r="5" fill="none" stroke="#555" stroke-width="1.6"/><line x1="21.5" y1="21.5" x2="25" y2="25" stroke="#555" stroke-width="1.6"/></svg>
  </div>
  <a class="abs top-link" style="left:638px">Subscribe to our Weekly Bulletin</a>
  <a class="abs top-link" style="left:857px">Register to Add Events</a>
  <a class="abs login">LOGIN</a>
</header>

<nav class="abs nav">
  <ul>
    <li class="active">HOME</li>
    <li>LATEST NEWS</li>
    <li>UPCOMING EVENT</li>
    <li>OUR DIARY</li>
    <li>CALENDAR</li>
    <li>BLOG</li>
    <li>CONTACT</li>
  </ul>
</nav>

<section class="abs hero" role="img" aria-label="Photo of a woman walking along a busy city street">
  <div class="abs hero-text">
    <h1>WELCOME TO MEETDIARY</h1>
    <p>We are an online diary/calendar and a resource for networking event</p>
  </div>
  <div class="abs dots"><span class="on"></span><span></span><span></span></div>
</section>

<!-- Networking tips -->
<h2 class="abs sec-title" style="left:100px;top:636px">Networking Tips</h2>
<div class="abs arrows">
  <span><svg width="8" height="12"><path d="M7 1 2 6l5 5" fill="none" stroke="#999" stroke-width="1.5"/></svg></span>
  <span><svg width="8" height="12"><path d="M1 1l5 5-5 5" fill="none" stroke="#999" stroke-width="1.5"/></svg></span>
</div>

<article class="abs tip" style="left:100px;top:703px"><div class="ph" role="img" aria-label="City square with a tall column" style="background:linear-gradient(180deg,#b8c3cc,#8e8a80)"></div><h3>Lorem Ipsum is simply dummy<br>text of the printing</h3><p>Lorem Ipsum is simply dummy text of the printing and typesetting industry. been the industry's...</p></article>
<article class="abs tip" style="left:348px;top:703px"><div class="ph" role="img" aria-label="Black and white silhouette by the sea" style="background:linear-gradient(180deg,#d9d9d9,#3a3a3a)"></div><h3>Lorem Ipsum is simply dummy<br>text of the printing</h3><p>Lorem Ipsum is simply dummy text of the printing and typesetting industry. been the industry's...</p></article>
<article class="abs tip" style="left:596px;top:703px"><div class="ph" role="img" aria-label="Black and white station platform" style="background:linear-gradient(180deg,#e2e2e2,#4a4a4a)"></div><h3>Lorem Ipsum is simply dummy<br>text of the printing</h3><p>Lorem Ipsum is simply dummy text of the printing and typesetting industry. been the industry's...</p></article>
<article class="abs tip" style="left:100px;top:998px"><div class="ph" role="img" aria-label="Car dashboard with navigation screen" style="background:linear-gradient(180deg,#6e7a84,#1d2328)"></div><h3>Lorem Ipsum is simply dummy<br>text of the printing</h3><p>Lorem Ipsum is simply dummy text of the printing and typesetting industry. been the industry's...</p></article>
<article class="abs tip" style="left:348px;top:998px"><div class="ph" role="img" aria-label="Airliner in a blue sky" style="background:linear-gradient(180deg,#3f74b5,#a9c7e6)"></div><h3>Lorem Ipsum is simply dummy<br>text of the printing</h3><p>Lorem Ipsum is simply dummy text of the printing and typesetting industry. been the industry's...</p></article>
<article class="abs tip" style="left:596px;top:998px"><div class="ph" role="img" aria-label="Old world map in warm brown tones" style="background:linear-gradient(135deg,#5a3a1c,#b07a36)"></div><h3>Lorem Ipsum is simply dummy<br>text of the printing</h3><p>Lorem Ipsum is simply dummy text of the printing and typesetting industry. been the industry's...</p></article>

<div class="abs banner" role="img" aria-label="Advertising banner for free video tutorials"></div>

<!-- Upcoming events -->
<h2 class="abs sec-title" style="left:100px;top:1416px">Upcoming Events</h2>

<article class="abs event" style="top:1487px"><div class="ph" role="img" aria-label="Canal city skyline at dusk" style="background:linear-gradient(180deg,#8fb3d6,#b58a5c)"></div><div class="body"><h3>Lorem Ipsum is simply dummy ext of the printing</h3><div class="meta"><span>&#9679; 27 MARCH 2015</span><span>&#9675; 120</span><span>&#9675; 200</span></div><p>Lorem Ipsum is simply dummy text of the printing and typesetting industry. Lorem Ipsum has been the industry's standard dummy text ever since the 1500s, when an unknown printer took a galley of type and scrambled it to make a type specimen book. It has survived not only five centuries, but also the leap...</p></div></article>
<article class="abs event" style="top:1707px"><div class="ph" role="img" aria-label="High-speed train in motion" style="background:linear-gradient(135deg,#9aa4ad,#5b6470)"></div><div class="body"><h3>Lorem Ipsum is simply dummy ext of the printing</h3><div class="meta"><span>&#9679; 27 MARCH 2015</span><span>&#9675; 120</span><span>&#9675; 200</span></div><p>Lorem Ipsum is simply dummy text of the printing and typesetting industry. Lorem Ipsum has been the industry's standard dummy text ever since the 1500s, when an unknown printer took a galley of type and scrambled it to make a type specimen book. It has survived not only five centuries, but also the leap...</p></div></article>
<article class="abs event" style="top:1927px"><div class="ph" role="img" aria-label="Two colleagues talking at a desk" style="background:linear-gradient(135deg,#d8d2c8,#7d6a62)"></div><div class="body"><h3>Lorem Ipsum is simply dummy ext of the printing</h3><div class="meta"><span>&#9679; 27 MARCH 2015</span><span>&#9675; 120</span><span>&#9675; 200</span></div><p>Lorem Ipsum is simply dummy text of the printing and typesetting industry. Lorem Ipsum has been the industry's standard dummy text ever since the 1500s, when an unknown printer took a galley of type and scrambled it to make a type specimen book. It has survived not only five centuries, but also the leap...</p></div></article>
<article class="abs event" style="top:2147px"><div class="ph" role="img" aria-label="Two women chatting on a street" style="background:linear-gradient(135deg,#7f98b0,#3c3f45)"></div><div class="body"><h3>Lorem Ipsum is simply dummy ext of the printing</h3><div class="meta"><span>&#9679; 27 MARCH 2015</span><span>&#9675; 120</span><span>&#9675; 200</span></div><p>Lorem Ipsum is simply dummy text of the printing and typesetting industry. Lorem Ipsum has been the industry's standard dummy text ever since the 1500s, when an unknown printer took a galley of type and scrambled it to make a type specimen book. It has survived not only five centuries, but also the leap...</p></div></article>
<article class="abs event" style="top:2367px;border-bottom:0"><div class="ph" role="img" aria-label="Man in glasses and bow tie on a light background" style="background:linear-gradient(135deg,#f0ebe6,#d6564a)"></div><div class="body"><h3>Lorem Ipsum is simply dummy ext of the printing</h3><div class="meta"><span>&#9679; 27 MARCH 2015</span><span>&#9675; 120</span><span>&#9675; 200</span></div><p>Lorem Ipsum is simply dummy text of the printing and typesetting industry. Lorem Ipsum has been the industry's standard dummy text ever since the 1500s, when an unknown printer took a galley of type and scrambled it to make a type specimen book. It has survived not only five centuries, but also the leap...</p></div></article>

<div class="abs pager"><span>Prev</span><span>1</span><span>2</span><span>3</span><span>4</span><span>5</span><span>6</span><span>...</span><span>22</span><span>Next</span></div>

<!-- Networking news -->
<h2 class="abs" style="left:100px;top:2635px;font-size:15px;font-weight:700;color:var(--heading)">NETWORKING NEWS</h2>
<article class="abs news" style="left:100px;top:2700px"><h3>Lorem Ipsum is simply dummy ext<br>of the printing</h3><div class="bar"></div><p>Lorem Ipsum is simply dummy text of the printing and typesetting industry. Lorem Ipsum has been the industry's standard dummy text ever since the 1500s, when an un-known printer took a galley...</p></article>
<article class="abs news" style="left:480px;top:2700px"><h3>Lorem Ipsum is simply dummy ext<br>of the printing</h3><div class="bar"></div><p>Lorem Ipsum is simply dummy text of the printing and typesetting industry. Lorem Ipsum has been the industry's standard dummy text ever since the 1500s, when an un-known printer took a galley...</p></article>
<article class="abs news" style="left:100px;top:2913px"><h3>Lorem Ipsum is simply dummy ext<br>of the printing</h3><div class="bar"></div><p>Lorem Ipsum is simply dummy text of the printing and typesetting industry. Lorem Ipsum has been the industry's standard dummy text ever since the 1500s, when an un-known printer took a galley...</p></article>
<article class="abs news" style="left:480px;top:2913px"><h3>Lorem Ipsum is simply dummy ext<br>of the printing</h3><div class="bar"></div><p>Lorem Ipsum is simply dummy text of the printing and typesetting industry. Lorem Ipsum has been the industry's standard dummy text ever since the 1500s, when an un-known printer took a galley...</p></article>

<!-- Sidebar -->
<aside>
  <h2 class="abs side-title" style="left:845px;top:636px">Follow Us</h2>
  <p class="abs" style="left:845px;top:684px;font-size:10px">Connect with our social media</p>
  <div class="abs social" style="left:845px;top:712px">
    <span style="background:#3b5998"></span><span style="background:#29a9e1"></span><span style="background:#dd4b39"></span><span style="background:#0e76a8"></span><span style="background:#cb2027"></span><span style="background:#e4405f"></span><span style="background:#f26522"></span>
  </div>

  <h2 class="abs side-title" style="left:845px;top:768px;border:0">Event Calender</h2>
  <div class="abs cal">
    <div class="cal-head">
      <span><svg width="6" height="10"><path d="M5 1 1 5l4 4" fill="none" stroke="#fff" stroke-width="1.5"/></svg></span>
      <b>DECEMBER</b>
      <span><svg width="6" height="10"><path d="M1 1l4 4-4 4" fill="none" stroke="#fff" stroke-width="1.5"/></svg></span>
    </div>
    <div class="cal-card">
      <div class="ph" role="img" aria-label="Event thumbnail"></div>
      <b>LOREM IPSUM IS SIMPLY DUMMY</b>
      <i>On 30 november 2015</i>
    </div>
    <div class="cal-days"><span>29</span><span class="on">30</span><span>1</span><span>2</span><span>3</span><span>4</span><span>5</span><span>6</span></div>
  </div>

  <div class="abs promo" style="top:1032px">
    <div class="ph" role="img" aria-label="Office colleagues smiling at a laptop" style="background:linear-gradient(135deg,#eef2f6,#a9b8c8)"></div>
    <div class="cap"><b>SUBSCRIBE</b><span>Subscribe to our Event &raquo;</span></div>
  </div>
  <div class="abs promo" style="top:1288px">
    <div class="ph" role="img" aria-label="Woman working at a desk" style="background:linear-gradient(135deg,#f4f4f2,#b9b3a8)"></div>
    <div class="cap"><b>REGISTER</b><span>Register to Add Events &raquo;</span></div>
  </div>

  <div class="abs ad-side" style="top:1545px;height:214px;background:linear-gradient(180deg,#1f4fa0 0%,#1f4fa0 35%,#c8d3e3 35%,#e7ecf3 100%)" role="img" aria-label="Advertisement for web hosting servers"></div>

  <h2 class="abs side-title" style="left:845px;top:1784px;border:0">Video Gallery</h2>
  <div class="abs vids">
    <div class="vid" role="img" aria-label="Video thumbnail of a meeting" style="background:linear-gradient(135deg,#c9d1da,#6e7c8a)"><svg width="30" height="30"><circle cx="15" cy="15" r="15" fill="rgba(255,255,255,.85)"/><path d="M12 9v12l9-6z" fill="#c0392b"/></svg></div>
    <div class="vid" role="img" aria-label="Video thumbnail of a beach" style="background:linear-gradient(135deg,#7fb9e0,#e8dcc0)"><svg width="30" height="30"><circle cx="15" cy="15" r="15" fill="rgba(255,255,255,.85)"/><path d="M12 9v12l9-6z" fill="#c0392b"/></svg></div>
    <div class="vid" role="img" aria-label="Video thumbnail of people talking" style="background:linear-gradient(135deg,#5a6a7c,#b3bcc5)"><svg width="30" height="30"><circle cx="15" cy="15" r="15" fill="rgba(255,255,255,.85)"/><path d="M12 9v12l9-6z" fill="#c0392b"/></svg></div>
    <div class="vid" role="img" aria-label="Video thumbnail of a group" style="background:linear-gradient(135deg,#d3c7bb,#8d7b6c)"><svg width="30" height="30"><circle cx="15" cy="15" r="15" fill="rgba(255,255,255,.85)"/><path d="M12 9v12l9-6z" fill="#c0392b"/></svg></div>
    <div class="vid" role="img" aria-label="Video thumbnail of an office" style="background:linear-gradient(135deg,#e4e0d8,#9b8f83)"><svg width="30" height="30"><circle cx="15" cy="15" r="15" fill="rgba(255,255,255,.85)"/><path d="M12 9v12l9-6z" fill="#c0392b"/></svg></div>
    <div class="vid" role="img" aria-label="Video thumbnail of a presenter" style="background:linear-gradient(135deg,#f1e6dc,#c2a48e)"><svg width="30" height="30"><circle cx="15" cy="15" r="15" fill="rgba(255,255,255,.85)"/><path d="M12 9v12l9-6z" fill="#c0392b"/></svg></div>
  </div>
  <a class="abs more">VIEW MORE VIDEOS</a>

  <div class="abs tweets">
    <div class="tw-head"><b>Tweets</b><span>Follow</span></div>
    <div class="tw"><div class="av"></div><p><b>Lorem Ipsum is simply</b> dummy text of the printing and typesetting...</p></div>
    <div class="tw"><div class="av"></div><p><b>Lorem Ipsum is simply</b> dummy text of the printing and typesetting...</p></div>
    <div class="tw"><div class="av"></div><p><b>Lorem Ipsum is simply</b> dummy text of the printing and typesetting...</p></div>
    <div class="tw"><div class="av"></div><p><b>Lorem Ipsum is simply</b> dummy text of the printing and typesetting...</p></div>
    <div class="tw-input">Tweet to @meetdiary</div>
  </div>

  <div class="abs ad-side" style="top:2691px;height:216px;background:linear-gradient(180deg,#2f6fc0 0%,#6aa4e0 55%,#f2c21b 55%,#f5d24a 100%)" role="img" aria-label="Advertisement for family web hosting plans"></div>
</aside>

<footer class="abs footer">
  <div class="abs f-col" style="left:108px">
    <h4>Quick links</h4>
    <ul><li>About Us</li><li>What We Do</li><li>How we work</li><li>Blog Post</li><li>News &amp; Events</li></ul>
  </div>
  <div class="abs f-col" style="left:335px">
    <h4>Resources</h4>
    <ul><li>Mauris vel lacus</li><li>Vitae felis vestibulum</li><li>Aoluttpat imperdiet</li><li>Cum sociis</li><li>Natoque penatibus</li></ul>
  </div>
  <div class="abs f-col" style="left:565px">
    <h4>Newsletters Sign Up</h4>
    <p>Plesae sign up here for latest news</p>
    <div class="f-input"><svg width="14" height="10"><rect x=".5" y=".5" width="13" height="9" fill="none" stroke="#888"/><path d="M1 1l6 5 6-5" fill="none" stroke="#888"/></svg>Email address</div>
    <div class="f-btn">Subscribe</div>
  </div>
  <div class="abs f-col" style="left:928px">
    <h4>Stay in touch</h4>
    <div class="f-social"><span></span><span></span><span></span></div>
  </div>
</footer>
<div class="abs bottom"><p>&copy; 2015 Company Name &nbsp;All right reserved &nbsp;Term of Use</p></div>

</body>
</html>
```